We need a design for our website called Mivelda which is a brazilian e-commerce focused on childrenswear. Basically your are able to swap (sell & buy) your kids outgrown clothes in the website and we will offer all the necessary services to help you on that.

We believe the main characteristic of the company is the swap of clothes and accessories, but we also feel that by doing this we are guaranteeing that this clothes are not going to trash, reducing clothes waste and being friendly with the environment.

We believe it should be clean with solid and soft colors (refer to the logo attached) and should communicate high quality standards and trust.

We need 2 web pages: home/search results and product details. In both pages we would like to have a fixed top bar with the logo, menu (Buy, Sell, About Us), login, a short message and shopping cart. As well as a footer on the botton with different options and social network links.

- Home/search results: right at the beginning of the page we would like to have a welcome/explanatory carousel banner. It should be a conventional 2 columns design with filters on the left (~25%) and the results on the main section (~3/4 products per row). We need filters for clothes and accessories (size,category, brands, color, gender).

- Product details: again, this should be very clean, with breadcrumbs on the top, a very short description (product's name, category, size), price, "Add to cart" button, an image with zoom functionality (as reference: jquery jqzoom), a "Similar Items" box and a share bar (chatloom, quibbly, snapquilt, v+).

Please bear in mind that we plan to use the main template in different colors across the website.
Updates

Hi everyone! 

We have just updated the brief to add some "Must have features" and "Nice to have features". Please take a careful look at it as it affects pretty much every design we received so far.

We will guarantee the project in the next 1-2 days, but we first would like to see some initial proposals for the second page (product details). Some of you guys are doing an awesome job in the home page!

Best,

Mivelda team

We have just updated the contest payment status: it is now committed!

Best,
Mivelda Team

Target Market(s)

The main audience will be parents of any age

Industry/Entity Type

E-Commerce

Requirements
Must have
• We would like to have only the following elements in the header: logo, login, cart image, Home, "Compre" (Buy), "Venda" (Sell) - not necessarily in this order
- The header should be persistent all over the website (always fixed at the top), thus, if it is too thick it will end up eating too much vertical space in some pages
- The current page should be somehow highlited in the header
- Right next to the cart image on the top we need a small tag indicating how many itens are already inside the cart
- We need a button "Entenda como funcionamos" (which in english means "Learn more") in the banner
- Please use an image of childrens in the banner (not clothes or teenagers)
- Besides the banner, the user in a1024x768 screen resolution should at least be able to view the first row of search results
- There is no need for a "Add to cart" button in every search result (keep price, size, type only). This option should only be available in the second page (product details)
- When needed use "Adicionar ao carrinho" (portuguese) instead of "Add to cart" (english)
- Regarding social network links in the footer, we only need chatloom, quibbly, snapquilt, v+
- In the search results page we need an option to show 12, 24, 48 results per page
- Users need to be able to sort the results (newest first, price low-high and high-low)
Nice to have
• We don´t need a text search box anywhere in the website
- There is no need to present the payment methods in neither pages
- The image of the cart should be modified when there are items inside (full vs empty)
- When the user moves the mouse over the cart image, a simple "div" should show up bellow it listing all items
- Regarding social network links, we like icons that change colors when the user
moves the mouse over them
- Regarding the color scheme, use up to a max of 3 colors and feel free to change the logo colors if you find a better combination than the ones we provided

```html
<!DOCTYPE html>
<html lang="en">
<head>
<meta charset="utf-8">
<title>Mivelda – Clothes and Accessories</title>
<link href="https://fonts.googleapis.com/css2?family=Source+Sans+3:wght@400;600&display=swap" rel="stylesheet">
<style>
:root{
  --brand:#ec5a3e;
  --brand-dark:#c9452c;
  --price:#d9241c;
  --ink:#444;
  --muted:#666;
  --panel-grey:#d6d6d6;
  --line:#cfcfcf;
  --white:#fff;
  --side-pink:#f6d3d8;
}
*{box-sizing:border-box;margin:0;padding:0}
html,body{width:1200px;height:1146px;overflow:hidden}
body{position:relative;background:var(--white);font-family:"Source Sans 3",Arial,sans-serif;color:var(--ink)}
.abs{position:absolute}
.side-art{position:absolute;top:0;height:1146px;width:176px;background:linear-gradient(180deg,#f8dde1,#f3c9cf 50%,#f8dde1)}
.side-art.left{left:0}
.side-art.right{left:1024px}
.page{position:absolute;left:176px;top:0;width:848px;height:1146px;background:var(--white)}

.logo{left:190px;top:26px;font-size:50px;font-weight:400;color:var(--brand);letter-spacing:-0.5px;line-height:1}
.search{left:654px;top:51px;width:242px;height:21px;display:flex}
.search .field{flex:1;border:1px solid var(--line);font-size:8px;color:var(--muted);padding:5px 10px;text-transform:uppercase;background:#fafafa}
.search .go{width:54px;background:var(--brand);color:var(--white);font-size:10px;display:flex;align-items:center;justify-content:center}
.cart-box{left:912px;top:41px;width:100px;height:33px;border:1px solid var(--line);display:flex;align-items:center;gap:10px;padding-left:10px;font-size:10px;color:var(--muted)}

.nav{left:182px;top:94px;width:836px;height:39px;background:var(--brand)}
.nav a{position:absolute;top:12px;color:var(--white);text-decoration:none;font-size:13px}
.nav .small{font-size:9px;top:15px}
.badge{left:989px;top:89px;width:22px;height:14px;border-radius:50%;background:#f7b6bd;color:#8a3a3a;font-size:8px;text-align:center;line-height:14px}

.banner{left:182px;top:133px;width:836px;height:283px;background:linear-gradient(90deg,#d9d3cc,#efeceb 30%,#e8e4e1 60%,#d8d2cf)}
.caption{left:182px;top:360px;width:836px;height:56px;background:rgba(60,60,60,.85)}
.caption-text{left:206px;top:375px;color:var(--white);font-size:19px}
.cta{left:615px;top:370px;width:255px;height:40px;background:var(--brand);border-radius:3px;color:var(--white);font-size:19px;text-align:center;line-height:40px}
.dots{left:946px;top:384px;display:flex;gap:2px}
.dots span{width:10px;height:10px;background:#bbb}

.filters{left:186px;top:454px;width:193px;height:378px;background:var(--brand);border:2px solid var(--brand-dark);box-shadow:inset 0 0 0 2px #f08c79}
.filters h2{position:absolute;left:12px;top:18px;font-size:17px;font-weight:400;color:var(--white)}
.check{position:absolute;top:52px;font-size:10px;color:var(--white);display:flex;align-items:center;gap:4px}
.check i{width:9px;height:9px;background:var(--white);border:1px solid #ddd;display:block}
.flabel{position:absolute;left:18px;font-size:10px;color:var(--white)}
.select{position:absolute;left:16px;width:164px;height:18px;background:linear-gradient(#fff,#ececec);border:1px solid #ccc;font-size:8px;color:var(--muted);padding:4px 14px}
.select b{position:absolute;right:2px;top:2px;width:12px;height:12px;border:1px solid #aaa;background:#fff}
.select b::after{content:"";position:absolute;left:3px;top:4px;border:3px solid transparent;border-top:4px solid #333}
.find{position:absolute;left:90px;top:336px;width:87px;height:22px;background:linear-gradient(#f4f4f4,#d8d8d8);border:1px solid #aaa;border-radius:2px;font-size:10px;color:#555;text-align:center;line-height:20px}

.connect{left:192px;top:847px;font-size:12px;color:var(--ink)}
.connect-title{left:191px;top:863px;font-size:15px;color:var(--brand)}
.social{left:189px;width:192px;height:19px;border-radius:3px;color:var(--white);font-size:8.5px;line-height:19px;padding-left:62px}
.social::before{content:"";position:absolute;left:9px;top:5px;width:9px;height:9px;background:rgba(255,255,255,.85)}
.social.quibbly{top:890px;background:linear-gradient(#c7e3f6,#8fc2e8);color:#24527a;border:1px solid #7fb0d6}
.social.chatloom{top:922px;background:linear-gradient(#6f93c2,#3d5f95)}
.social.snapquilt{top:957px;background:linear-gradient(#ee2a2a,#c41010)}
.social.vplus{top:990px;background:linear-gradient(#3a8ef0,#1662c9)}

.results-bar{left:398px;top:455px;width:611px;height:35px;background:var(--panel-grey)}
.results-bar .t{position:absolute;left:22px;top:12px;font-size:10px;color:#555}
.results-bar .s{position:absolute;left:476px;top:13px;font-size:9px;color:#555}
.sortbox{position:absolute;left:525px;top:8px;width:74px;height:18px;background:var(--white);border:1px solid #bbb;font-size:8px;color:#999;padding:4px 9px}
.sortbox b{position:absolute;right:2px;top:2px;width:12px;height:12px;border:1px solid #aaa}
.sortbox b::after{content:"";position:absolute;left:3px;top:4px;border:3px solid transparent;border-top:4px solid #333}

.card{position:absolute;width:184px}
.card .photo{height:172px;border:1px solid #ccc}
.card p{margin-top:16px;font-size:8.5px;line-height:14px;color:var(--ink)}
.card .row{display:flex;justify-content:space-between;margin-top:10px;font-size:16px;color:var(--price)}

.pager{top:1040px;height:22px;border:1px solid #bbb;font-size:9px;text-align:center;line-height:20px;color:#444;background:linear-gradient(#fff,#e8e8e8);border-radius:2px}
.pager.red{background:var(--brand);color:var(--white);border-color:var(--brand-dark)}

.footer{left:181px;top:1086px;width:839px;height:60px;background:var(--brand)}
.footer nav{position:absolute;left:11px;top:23px;font-size:9px;color:var(--white);display:flex;gap:8px}
.footer nav span.sep{opacity:.9}
.footer .copy{position:absolute;right:18px;top:23px;font-size:8.5px;color:var(--white)}
</style>
</head>
<body>
<div class="side-art left" role="img" aria-label="Pink gingham pattern with playful drawings of a heart, a fairy, a girl with a cupcake, a bow and a teddy bear"></div>
<div class="side-art right" role="img" aria-label="Pink gingham pattern with playful drawings of a gift box, a cat, hearts, two teddy bears and a fairy"></div>
<div class="page"></div>

<div class="abs logo">Mivelda</div>

<div class="abs search"><div class="field">Enter your product keyword</div><div class="go">Search</div></div>
<div class="abs cart-box">
  <svg width="20" height="18" viewBox="0 0 20 18"><path d="M1 2h3l2.5 9h9l2-6.5H5.5" fill="none" stroke="#e0463a" stroke-width="1.8" stroke-linejoin="round"/><circle cx="8" cy="15" r="1.6" fill="#e0463a"/><circle cx="14.5" cy="15" r="1.6" fill="#e0463a"/></svg>
  <span>YOUR CART</span>
</div>

<nav class="abs nav">
  <a style="left:30px">Home</a>
  <a style="left:128px">Compre</a>
  <a style="left:236px">Buy</a>
  <a class="small" style="left:700px">My Account</a>
  <a class="small" style="left:762px">|</a>
  <a class="small" style="left:786px">My Cart</a>
</nav>
<div class="abs badge">8</div>

<div class="abs banner" role="img" aria-label="Photo of four young girls in colourful casual outfits sitting on a white sofa"></div>
<div class="abs caption"></div>
<div class="abs caption-text">Lorem Ipsum is simply dummy text of the printing.</div>
<div class="abs cta">Entenda como funcionamos</div>
<div class="abs dots"><span></span><span></span><span></span><span></span><span></span></div>

<aside class="abs filters">
  <h2>Clothes and Accessories</h2>
  <div class="check" style="left:14px"><i></i>Buy a Dress</div>
  <div class="check" style="left:88px"><i></i>Sell A Dress</div>
  <div class="flabel" style="top:84px">Dress For :</div>
  <div class="select" style="top:98px">BOY :<b></b></div>
  <div class="flabel" style="top:126px">Age :</div>
  <div class="select" style="top:139px">BOY :<b></b></div>
  <div class="flabel" style="top:167px">Size :</div>
  <div class="select" style="top:180px">BOY :<b></b></div>
  <div class="flabel" style="top:208px">Category :</div>
  <div class="select" style="top:221px">BOY :<b></b></div>
  <div class="flabel" style="top:250px">Brands :</div>
  <div class="select" style="top:264px">BOY :<b></b></div>
  <div class="flabel" style="top:291px">Color :</div>
  <div class="select" style="top:305px">BOY :<b></b></div>
  <div class="find">FIND DRESS</div>
</aside>

<div class="abs connect">Connect to</div>
<div class="abs connect-title">Our Social Network :</div>
<div class="abs social quibbly">Sign in with quibbly</div>
<div class="abs social chatloom">Sign in with chatloom</div>
<div class="abs social snapquilt">Sign in with snapquilt</div>
<div class="abs social vplus">Sign in with v+</div>

<div class="abs results-bar">
  <span class="t">SEARCH RESULTS</span>
  <span class="s">SORT BY :</span>
  <div class="sortbox">LATEST<b></b></div>
</div>

<div class="card" style="left:402px;top:504px">
  <div class="photo" role="img" aria-label="Photo of a smiling baby lying among colourful clothes" style="background:linear-gradient(135deg,#e8d2b8,#d9b89a)"></div>
  <p>Lorem Ipsum is simply dummy text of the<br>printing and typesetting industry</p>
  <div class="row"><span>$62.00</span><span>Size : 6</span></div>
</div>
<div class="card" style="left:610px;top:504px">
  <div class="photo" role="img" aria-label="Photo of a young girl in a red printed sweater" style="background:linear-gradient(180deg,#f4f1ee,#e9d6d2 60%,#c94a48)"></div>
  <p>Lorem Ipsum is simply dummy text of the<br>printing and typesetting industry</p>
  <div class="row"><span>$62.00</span><span>Size : 8</span></div>
</div>
<div class="card" style="left:820px;top:504px">
  <div class="photo" role="img" aria-label="Photo of a pink long-sleeved tulle dress" style="background:linear-gradient(135deg,#f8e6eb,#efb2c3)"></div>
  <p>Lorem Ipsum is simply dummy text of the<br>printing and typesetting industry</p>
  <div class="row"><span>$62.00</span><span>Size : 7</span></div>
</div>
<div class="card" style="left:402px;top:770px">
  <div class="photo" role="img" aria-label="Photo of two children in bright striped knitwear and scarves" style="background:linear-gradient(135deg,#f2efe9,#b54a3a 45%,#3d5b8c 70%,#e9e3da)"></div>
  <p>Lorem Ipsum is simply dummy text of the<br>printing and typesetting industry</p>
  <div class="row"><span>$62.00</span><span>Size : 6</span></div>
</div>
<div class="card" style="left:610px;top:770px">
  <div class="photo" role="img" aria-label="Photo of a smiling girl in a purple patterned dress" style="background:linear-gradient(180deg,#f7f5f4,#e6d4cc 55%,#5a3a6a)"></div>
  <p>Lorem Ipsum is simply dummy text of the<br>printing and typesetting industry</p>
  <div class="row"><span>$62.00</span><span>Size : 8</span></div>
</div>
<div class="card" style="left:820px;top:770px">
  <div class="photo" role="img" aria-label="Photo of a baby sitting in a pink ruffled dress" style="background:linear-gradient(180deg,#f6f2f1,#efc6cd)"></div>
  <p>Lorem Ipsum is simply dummy text of the<br>printing and typesetting industry</p>
  <div class="row"><span>$62.00</span><span>Size : 9</span></div>
</div>

<div class="abs pager red" style="left:713px;width:52px">« Prev</div>
<div class="abs pager" style="left:769px;width:22px">1</div>
<div class="abs pager" style="left:795px;width:22px">2</div>
<div class="abs pager" style="left:822px;width:22px">3</div>
<div class="abs pager red" style="left:848px;width:22px">...</div>
<div class="abs pager" style="left:875px;width:22px">4</div>
<div class="abs pager" style="left:902px;width:22px">5</div>
<div class="abs pager" style="left:928px;width:22px">6</div>
<div class="abs pager red" style="left:954px;width:52px">Next »</div>

<footer class="abs footer">
  <nav>
    <span>Home</span><span class="sep">|</span>
    <span>About Us</span><span class="sep">|</span>
    <span>Services</span><span class="sep">|</span>
    <span>Products</span><span class="sep">|</span>
    <span>Buy Dree</span><span class="sep">|</span>
    <span>Sell Dress</span><span class="sep">|</span>
    <span>Blog</span><span class="sep">|</span>
    <span>Contact Us</span>
  </nav>
  <div class="copy">Copyright © 2013. Mivelda. All Rights Reserved.</div>
</footer>
</body>
</html>
```